Brivora Australia Company Values.

We have just completed our company purpose, beliefs and values (for the first time, we have not had these before)
We are now wanting to add images to each company value as a visual
so they are easily identified and understood for all our staff - we need them to remember the 5 Values.
We are a manufacturer of dental materials and infection control products, based in Melbourne.

What we would like:
- A Poster (that can be placed in our staff lunch rooms)
- The values to be lined up Horizontally
- Image on the top of the words
- Wording does not all need to be the same text font
- No image photographs - please use image graphics
- No images with people
- No dental related graphics

Target audience: Brivora staff

Our Values are:
Think Big
Have a go, learn and adapt
If you're gonna do it, do it bloody well
Empower Others
Be a good human

I have uploaded some examples.

Target Market(s)

Brivora Team members

Industry/Entity Type

Healthcare

Colors

Designer to choose colors to be used in the design.

Requirements
Must have
• Clear horizontal layout, space between each value
Should not have
• No images with humans or dental

```html
<!DOCTYPE html>
<html lang="en">
<head>
<meta charset="utf-8">
<title>Brivora Australia – Company Values</title>
<link rel="stylesheet" href="https://fonts.googleapis.com/css2?family=Baloo+2:wght@700;800&family=Racing+Sans+One&family=Cinzel+Decorative:wght@400&display=swap">
<style>
  :root {
    --blue-deep: #0a3a92;
    --blue-mid: #1557c0;
    --blue-light: #2a7ae0;
    --gold: #f7b41b;
    --gold-text: #f4b223;
    --white: #ffffff;
    --grey-light: #eef0f2;
    --grey-mid: #d9dcdf;
  }
  html, body {
    margin: 0;
    padding: 0;
    overflow: hidden;
  }
  .poster {
    position: relative;
    width: 1200px;
    height: 807px;
    overflow: hidden;
    background: radial-gradient(circle at 70% 20%, var(--blue-light) 0%, var(--blue-mid) 40%, var(--blue-deep) 100%);
  }
  .backdrop-top, .backdrop-bottom {
    position: absolute;
    left: 0;
    width: 1200px;
  }
  .backdrop-top {
    top: 0;
    height: 151px;
    background: radial-gradient(ellipse at 65% 70%, #2b86ea 0%, #1556c0 45%, #0b3c96 100%);
  }
  .backdrop-bottom {
    top: 681px;
    height: 126px;
    background: radial-gradient(ellipse at 60% 20%, #2a80e6 0%, #1453bb 50%, #0a3a92 100%);
  }
  .gold-band {
    position: absolute;
    left: 0;
    width: 1200px;
    background: var(--gold);
  }
  .gold-band--top { top: 151px; height: 22px; }
  .gold-band--bottom { top: 662px; height: 19px; }
  .values-panel {
    position: absolute;
    left: 0;
    top: 173px;
    width: 1200px;
    height: 489px;
    background: linear-gradient(180deg, var(--grey-light) 0%, #f8f9fa 35%, var(--grey-mid) 100%);
  }
  .value-icon {
    position: absolute;
    top: 218px;
    width: 164px;
    height: 164px;
    margin-left: -87px;
    border: 5px solid var(--gold);
    border-radius: 50%;
    background: var(--white);
    display: flex;
    align-items: center;
    justify-content: center;
  }
  .value-icon .art {
    width: 124px;
    height: 110px;
    border-radius: 50%;
  }
  .art--brain { background: radial-gradient(circle, #f7a531 0%, #f8c77a 60%, #ffffff 100%); }
  .art--plane { background: linear-gradient(135deg, #4fd1b8 0%, #5cc9b0 45%, #fbbb13 100%); }
  .art--search { background: radial-gradient(circle, #ffffff 30%, #c8ccd6 60%, #ffffff 100%); }
  .art--hands { background: conic-gradient(#e9435f, #f7941d, #8dc63f, #27b4a8, #7a2a5c, #e9435f); }
  .art--seedling { background: linear-gradient(180deg, #7cbf3a 0%, #4a3a2a 55%, #e0a88a 100%); }

  .value-card {
    position: absolute;
    top: 418px;
    width: 182px;
    height: 177px;
    border: 5px solid var(--gold);
    border-radius: 30px;
    background: var(--white);
    display: flex;
    align-items: center;
    justify-content: center;
    text-align: center;
    color: var(--gold-text);
  }
  .value-card p { margin: 0; }
  .value-text--bold {
    font-family: "Baloo 2", sans-serif;
    font-weight: 800;
    font-size: 29px;
    line-height: 38px;
    text-transform: uppercase;
  }
  .value-text--racing {
    font-family: "Racing Sans One", sans-serif;
    font-style: italic;
    font-size: 24px;
    line-height: 34px;
    text-transform: uppercase;
    text-align: left;
  }
  .value-text--serif {
    font-family: "Cinzel Decorative", serif;
    font-size: 31px;
    line-height: 42px;
    text-transform: uppercase;
  }
</style>
</head>
<body>
  <main class="poster" aria-label="Brivora Australia company values">
    <div class="backdrop-top" role="img" aria-label="Blue technology pattern background"></div>
    <div class="gold-band gold-band--top"></div>
    <div class="values-panel" role="img" aria-label="Soft white hexagon block background"></div>
    <div class="gold-band gold-band--bottom"></div>
    <div class="backdrop-bottom" role="img" aria-label="Blue technology pattern background"></div>

    <div class="value-icon" style="left:135px"><div class="art art--brain" role="img" aria-label="Glowing brain lightbulb graphic"></div></div>
    <div class="value-icon" style="left:361px"><div class="art art--plane" role="img" aria-label="Paper plane graphic"></div></div>
    <div class="value-icon" style="left:600px"><div class="art art--search" role="img" aria-label="Magnifying glass graphic"></div></div>
    <div class="value-icon" style="left:846px"><div class="art art--hands" role="img" aria-label="Circle of colourful linked hands graphic"></div></div>
    <div class="value-icon" style="left:1084px"><div class="art art--seedling" role="img" aria-label="Seedling held in an open palm graphic"></div></div>

    <div class="value-card" style="left:29px"><p class="value-text--bold">Think Big</p></div>
    <div class="value-card" style="left:262px"><p class="value-text--bold">Have a go,<br>learn &amp;<br>adapt</p></div>
    <div class="value-card" style="left:507px"><p class="value-text--racing">If you're<br>&nbsp;gonna do it,<br>&nbsp;&nbsp;&nbsp;do it<br>&nbsp;bloody well</p></div>
    <div class="value-card" style="left:747px"><p class="value-text--serif">Empower<br>Others</p></div>
    <div class="value-card" style="left:983px"><p class="value-text--bold">Be a good<br>human</p></div>
  </main>
</body>
</html>
```